2021 Halberd Ensemble Summer Music Institute & Festival

we need a brochure for the Summer music school and series of concerts. We want it to be modern, and informative. Please look at our web page:
http://academy.halberdensemble.org/halberd-summer-music-institute/

Target Market(s)

middle-class families with school and college children

Requirements
Must have
• text from the web page:
Also
http://halberdensemble.org/category/2021-halberd-summer-music-festival/
(this will be updated soon, but the events have to be listed in the brochure
Please use graphics from the pages and the attached files.

```html
<!DOCTYPE html>
<html lang="en">
<head>
<meta charset="utf-8">
<title>Halberd Ensemble Summer Music Institute &amp; Festival — Brochure</title>
<link href="https://fonts.googleapis.com/css2?family=Cinzel:wght@500;600;700&family=Montserrat:wght@400;500;600;700&display=swap" rel="stylesheet">
<style>
:root{
  --backdrop:#e4e4e2;
  --ink:#2a2a2d;
  --ink-soft:#3a3a3e;
  --gold:#c9a646;
  --gold-light:#e2c877;
  --paper:#ffffff;
  --text-light:#e9e9ea;
  --text-muted:#b9b9bc;
  --body:#4a4a4e;
}
*{box-sizing:border-box;margin:0;padding:0}
html,body{width:1200px;height:2704px;overflow:hidden}
body{background:var(--backdrop);font-family:"Montserrat",sans-serif;color:var(--ink);position:relative}

.page{position:absolute;background:var(--paper);overflow:hidden;box-shadow:0 2px 10px rgba(0,0,0,.12)}
.cover{width:620px;height:826px}
.cover--single{left:290px;top:40px}
.spread{position:absolute;left:30px;width:1140px;height:760px}
.spread--outer{top:920px}
.spread--inner{top:1740px}
.spread .page{width:570px;height:760px;top:0}
.spread .page--left{left:0}
.spread .page--right{left:570px}
.cover--scaled{width:620px;height:826px;transform:scale(.9194);transform-origin:0 0;box-shadow:none}
.spread-fold{position:absolute;left:569px;top:0;width:2px;height:760px;background:linear-gradient(90deg,rgba(0,0,0,.08),rgba(0,0,0,0));z-index:5}

.photo{position:absolute}
.cover__photo{left:0;top:30px;width:620px;height:580px;background:radial-gradient(ellipse at 62% 45%,#7a4a2c 0%,#4b2c1d 35%,#2a1b14 70%),linear-gradient(90deg,#b58a48,#5a3a22)}
.cover__shapes{position:absolute;left:0;top:0;width:620px;height:826px}
.brand{position:absolute;display:flex;align-items:center;gap:10px;font-family:"Montserrat",sans-serif;font-weight:600;color:var(--ink)}
.brand__dot{width:14px;height:14px;border-radius:50%;background:var(--gold)}
.cover__brand{left:46px;top:62px;font-size:17px;letter-spacing:.5px}
.cover__title{position:absolute;left:40px;right:40px;top:640px;text-align:center;font-family:"Cinzel",serif;font-weight:600;color:var(--paper);font-size:21px;line-height:1.45;letter-spacing:1px}
.url-bar{position:absolute;background:var(--gold);color:var(--ink);font-size:9px;font-weight:600;text-align:center;display:flex;align-items:center;justify-content:center;letter-spacing:.2px}
.cover__url{left:110px;right:110px;top:754px;height:22px}

/* back cover */
.back__shapes{position:absolute;left:0;top:0;width:570px;height:760px}
.back__heading{position:absolute;left:34px;top:48px;font-family:"Cinzel",serif;font-weight:700;font-size:15px;color:var(--ink);line-height:1.35}
.back__heading small{display:block;font-family:"Montserrat",sans-serif;font-size:9px;font-weight:500;color:var(--gold);letter-spacing:1px;margin-top:4px}
.back__info{position:absolute;left:34px;top:170px;width:250px;color:var(--text-light);font-size:8.5px;line-height:1.55}
.back__info h3{font-size:10px;color:var(--gold-light);font-weight:600;margin:10px 0 3px;letter-spacing:.5px}
.back__photo{left:300px;top:190px;width:236px;height:180px;background:linear-gradient(135deg,#556048,#8a8a6a 45%,#3b3f35)}
.back__note{position:absolute;left:300px;top:384px;width:236px;color:var(--text-muted);font-size:8px;line-height:1.55}
.back__brand{left:40px;top:648px;font-size:13px}
.back__url{left:180px;right:40px;top:712px;height:18px;font-size:8px}

/* inner spread */
.inner__photo-left{left:0;top:0;width:570px;height:330px;background:linear-gradient(160deg,#9aa59a 0%,#5d6b63 45%,#3a4340 100%)}
.inner__photo-right{left:0;top:0;width:570px;height:300px;background:radial-gradient(ellipse at 50% 60%,#c23a7a 0%,#7a2a6a 40%,#2c1f3e 80%)}
.inner__inset{left:420px;top:250px;width:120px;height:80px;border:3px solid var(--paper);background:linear-gradient(135deg,#6b5a3a,#3a2e20)}
.section-tag{position:absolute;background:var(--gold);color:var(--ink);font-family:"Cinzel",serif;font-weight:700;font-size:12px;padding:7px 16px;letter-spacing:.5px}
.inner__tag-left{left:34px;top:350px}
.inner__text{position:absolute;color:var(--body);font-size:8.5px;line-height:1.6}
.inner__text h4{font-size:9.5px;color:var(--ink);font-weight:700;margin:8px 0 2px}
.inner__text-left{left:34px;top:395px;width:500px}
.panel{position:absolute;left:34px;top:320px;width:502px;background:var(--ink);border-radius:4px;padding:16px 20px;color:var(--text-light)}
.panel h3{font-family:"Cinzel",serif;font-size:13px;color:var(--gold-light);margin-bottom:8px}
.panel ul{list-style:none;font-size:8.5px;line-height:1.75}
.panel li{display:flex;gap:8px;align-items:center}
.panel li::before{content:"";width:5px;height:5px;background:var(--gold);flex:none}
.inner__text-right{left:34px;top:520px;width:500px}
.page-bar{position:absolute;left:0;right:0;bottom:0;height:10px;background:var(--gold)}
</style>
</head>
<body>

<!-- Front cover -->
<section class="page cover cover--single">
  <div class="photo cover__photo" role="img" aria-label="Photo of a violinist wearing a mask, playing in a church with stained-glass windows"></div>
  <svg class="cover__shapes" viewBox="0 0 620 826" aria-hidden="true">
    <path d="M0,0 H620 V30 Q330,40 0,170 Z" fill="#ffffff"/>
    <path d="M0,555 Q300,470 620,505 V826 H0 Z" fill="#c9a646"/>
    <path d="M0,572 Q300,492 620,522 V826 H0 Z" fill="#2a2a2d"/>
  </svg>
  <div class="brand cover__brand"><span class="brand__dot"></span>Halberd Ensemble</div>
  <h1 class="cover__title">Halberd Ensemble Music Academy<br>Summer Institute and Festival</h1>
  <div class="url-bar cover__url">http://academy.halberdensemble.org/halberd-summer-music-institute/</div>
</section>

<!-- Outer spread: back + front -->
<section class="spread spread--outer">
  <article class="page page--left">
    <svg class="back__shapes" viewBox="0 0 570 760" aria-hidden="true">
      <path d="M0,130 Q280,160 570,120 V600 Q280,560 0,640 Z" fill="#2a2a2d"/>
      <path d="M0,640 Q280,560 570,600 V612 Q280,574 0,652 Z" fill="#c9a646"/>
      <path d="M0,122 Q280,152 570,112 V120 Q280,160 0,130 Z" fill="#c9a646"/>
    </svg>
    <h2 class="back__heading">2021 Halberd Ensemble<br>Summer Music Festival<small>INSTITUTE · CONCERTS · MASTERCLASSES</small></h2>
    <div class="back__info">
      <h3>Institute Dates</h3>
      <p>June 21 – July 31, 2021. Daily lessons, chamber coaching and orchestra rehearsals for young string players.</p>
      <h3>Who May Apply</h3>
      <p>Students aged 10 to 22, from school and college, of intermediate to advanced level.</p>
      <h3>Programme</h3>
      <p>Private lessons, chamber music, theory classes, performance workshops and weekly student concerts.</p>
      <h3>Faculty</h3>
      <p>Members of the ensemble and guest artists teaching violin, viola, cello and piano.</p>
      <h3>Tuition</h3>
      <p>Full and partial scholarships available. Apply online before May 15.</p>
    </div>
    <div class="photo back__photo" role="img" aria-label="Photo of students rehearsing chamber music outdoors"></div>
    <p class="back__note">Festival concerts are held every weekend in churches and gardens across the region. Families are warmly invited to attend.</p>
    <div class="brand back__brand"><span class="brand__dot"></span>Halberd Ensemble</div>
    <div class="url-bar back__url">http://halberdensemble.org/category/2021-halberd-summer-music-festival/</div>
  </article>

  <article class="page page--right">
    <div class="page cover cover--scaled">
      <div class="photo cover__photo" role="img" aria-label="Photo of a violinist wearing a mask, playing in a church with stained-glass windows"></div>
      <svg class="cover__shapes" viewBox="0 0 620 826" aria-hidden="true">
        <path d="M0,0 H620 V30 Q330,40 0,170 Z" fill="#ffffff"/>
        <path d="M0,555 Q300,470 620,505 V826 H0 Z" fill="#c9a646"/>
        <path d="M0,572 Q300,492 620,522 V826 H0 Z" fill="#2a2a2d"/>
      </svg>
      <div class="brand cover__brand"><span class="brand__dot"></span>Halberd Ensemble</div>
      <h2 class="cover__title">Halberd Ensemble Music Academy<br>Summer Institute and Festival</h2>
      <div class="url-bar cover__url">http://academy.halberdensemble.org/halberd-summer-music-institute/</div>
    </div>
  </article>
  <div class="spread-fold"></div>
</section>

<!-- Inner spread -->
<section class="spread spread--inner">
  <article class="page page--left">
    <div class="photo inner__photo-left" role="img" aria-label="Photo of musicians performing on an outdoor stage with an audience"></div>
    <div class="section-tag inner__tag-left">2021 Halberd Summer Music Festival</div>
    <div class="inner__text inner__text-left">
      <p>Each summer the ensemble opens its doors to young musicians who wish to grow as performers. Students live music every day, learning from professionals in a friendly setting.</p>
      <h4>Daily Schedule</h4>
      <p>Mornings begin with technique and private lessons. Afternoons are for chamber groups and orchestra. Evenings bring recitals and open rehearsals.</p>
      <h4>Concert Series</h4>
      <p>Our festival concerts pair faculty with gifted students in varied repertoire, from baroque to new works by living composers.</p>
      <h4>Location</h4>
      <p>Classes take place in historic halls with fine acoustics, close to parks, cafés and public transport.</p>
    </div>
    <div class="page-bar"></div>
  </article>

  <article class="page page--right">
    <div class="photo inner__photo-right" role="img" aria-label="Photo of an ensemble on a stage lit in red and purple light"></div>
    <div class="photo inner__inset" role="img" aria-label="Small photo of a string quartet in concert"></div>
    <div class="panel">
      <h3>2021 Summer Music Festival</h3>
      <ul>
        <li>June 26 — Opening Gala Concert</li>
        <li>July 3 — Baroque Evening by Candlelight</li>
        <li>July 10 — Student Chamber Showcase</li>
        <li>July 17 — Strings in the Garden</li>
        <li>July 24 — Faculty Recital Series</li>
        <li>July 31 — Closing Festival Concert</li>
      </ul>
    </div>
    <div class="inner__text inner__text-right">
      <p>Tickets are available online and at the door. Students of the institute enter free of charge.</p>
      <h4>How to Apply</h4>
      <p>Submit the online form with a short video recording and a teacher reference. Auditions are reviewed weekly.</p>
    </div>
    <div class="page-bar"></div>
  </article>
  <div class="spread-fold"></div>
</section>

</body>
</html>
```